New website for engineering consultant

We need to update our existing web site. We've just had our logo re-done and have attached it.

We are an engineering consulting firm that specialises in mechanical and structural engineering, design and drafting. Our customers are other businesses in the manufacturing, mining and agricultural industries.

We would like the designs to be professional and highlight that we are innovative.

Industry/Entity Type

Mining

Requirements
Must have
• A module that rotates pictures so we can showcase certain projects. We have attached a few rendered images of projects for you to play with.

```html
<!DOCTYPE html>
<html lang="en">
<head>
<meta charset="utf-8">
<title>Torque-Line Pty Ltd — Engineering Sustainable Futures</title>
<link href="https://fonts.googleapis.com/css2?family=Ubuntu:wght@400;500&display=swap" rel="stylesheet">
<style>
:root{
  --bg-deep:#020a3a;
  --bg-mid:#0a3aa8;
  --panel:#0b2a6e;
  --panel-edge:#1e54b8;
  --header:#f4f4f4;
  --brand:#1b2f8f;
  --nav:#1a3fa8;
  --text:#d9e2f5;
  --white:#ffffff;
  --link:#1f6cff;
  --yellow:#e2e23a;
}
*{margin:0;padding:0;box-sizing:border-box}
html,body{width:1200px;height:1125px;overflow:hidden}
body{
  position:relative;font-family:'Ubuntu',sans-serif;color:var(--text);
  background:radial-gradient(ellipse 700px 500px at 540px 340px,var(--bg-mid) 0%,#06237c 45%,var(--bg-deep) 100%);
}
.site-header{position:absolute;left:18px;top:17px;width:1163px;height:135px;background:var(--header)}
.brand{position:absolute;left:18px;top:12px;width:415px;height:109px;background:var(--white);border-radius:14px;display:flex;align-items:center;padding-left:22px;gap:14px}
.brand-mark{width:40px;height:40px;border-radius:50%;background:var(--brand)}
.brand-name{font-size:34px;font-weight:500;color:var(--brand);letter-spacing:-0.5px}
.main-nav{position:absolute;top:29px;left:0;width:100%;height:20px}
.main-nav a{position:absolute;font-size:15px;color:var(--nav);text-decoration:none;display:flex;align-items:center;gap:6px}
.main-nav svg{width:16px;height:14px}
.search{position:absolute;left:834px;top:77px;width:277px;height:35px;border:1px solid #9ab8e0;border-radius:18px;background:var(--white);box-shadow:0 0 4px #b8cfee;font-size:14px;color:#555;padding:8px 0 0 16px}
.search svg{position:absolute;right:12px;top:7px}
.hero-glow{position:absolute;left:230px;top:170px;width:560px;height:320px;border-radius:50%;background:radial-gradient(closest-side,rgba(70,150,255,.55),rgba(70,150,255,0))}
.hero-render{position:absolute;left:312px;top:206px;width:410px;height:230px;border-radius:10px;background:radial-gradient(ellipse at 45% 45%,rgba(226,226,58,.85) 0%,rgba(180,180,40,.55) 55%,rgba(60,100,180,0) 100%)}
.hero-title{position:absolute;left:665px;top:217px;font-size:24.5px;color:var(--white);font-weight:400;letter-spacing:.3px}
.hero-copy{position:absolute;left:732px;top:263px;width:352px;font-size:11.5px;line-height:14.5px;color:var(--text)}
.hero-rule{position:absolute;left:732px;top:312px;width:360px;height:1px;background:linear-gradient(90deg,rgba(120,170,255,.6),rgba(120,170,255,0))}
.slide-arrow{position:absolute;width:46px;height:46px;border-radius:50%;background:radial-gradient(circle at 40% 30%,#6fb4ec,#1f6fb8);box-shadow:0 2px 6px rgba(0,0,0,.4);display:flex;align-items:center;justify-content:center}
.content-panel{position:absolute;left:42px;top:497px;width:1116px;height:469px;border:2px solid var(--panel-edge);border-radius:20px;background:linear-gradient(180deg,#0d3384,var(--panel))}
.showcase-tab{position:absolute;left:917px;top:450px;width:229px;height:90px;border-radius:8px 16px 22px 4px;background:linear-gradient(180deg,#2ab7f5,#0e86d6);box-shadow:0 6px 10px rgba(0,0,0,.35);display:flex;align-items:center;padding-left:14px;gap:14px;color:var(--white);font-size:17.5px;font-weight:500;text-decoration:none}
.showcase-tab .dot{width:46px;height:46px;border-radius:50%;background:radial-gradient(circle at 40% 30%,#5a8fcf,#133f86);display:flex;align-items:center;justify-content:center}
.welcome-title{position:absolute;left:62px;top:518px;font-size:24px;font-weight:400;color:var(--white)}
.welcome-copy{position:absolute;left:62px;width:1062px;font-size:14px;line-height:17px;color:var(--text)}
.service-card{position:absolute;top:719px;width:264px;height:225px;border:1px solid #1c4aa8;border-radius:14px;background:linear-gradient(180deg,#123a8c,#0a2460)}
.service-card h2{position:absolute;font-size:15px;font-weight:400;color:var(--white);white-space:nowrap}
.service-card .art{position:absolute;border-radius:8px}
.service-card p{position:absolute;left:17px;width:226px;font-size:12px;line-height:14.5px;color:var(--text)}
.service-card .more{position:absolute;right:28px;font-size:12px;line-height:14px;color:var(--link);text-decoration:none}
.site-footer{position:absolute;left:58px;top:1010px;width:1103px;height:75px;border-radius:14px;background:linear-gradient(180deg,#0f3380,#0a2562)}
.copyright{position:absolute;left:30px;top:35px;font-size:12px;color:var(--white)}
.social{position:absolute;top:21px;width:33px;height:33px;border-radius:3px}
</style>
</head>
<body>

<header class="site-header">
  <div class="brand"><span class="brand-mark"></span><span class="brand-name">TORQUE-LINE</span></div>
  <nav class="main-nav">
    <a href="#" style="left:665px"><svg viewBox="0 0 16 14"><path d="M2 2v6h8v3l5-5-5-5v3H5" fill="#3a8fe0"/></svg>Home</a>
    <a href="#" style="left:775px"><svg viewBox="0 0 16 14"><path d="M2 2v6h8v3l5-5-5-5v3H5" fill="#3a8fe0"/></svg>About Us</a>
    <a href="#" style="left:897px"><svg viewBox="0 0 16 14"><path d="M2 2v6h8v3l5-5-5-5v3H5" fill="#3a8fe0"/></svg>Projects</a>
    <a href="#" style="left:1012px"><svg viewBox="0 0 16 14"><path d="M2 2v6h8v3l5-5-5-5v3H5" fill="#3a8fe0"/></svg>Contact Us</a>
  </nav>
  <div class="search">This is my new search
    <svg width="20" height="20" viewBox="0 0 20 20"><circle cx="8" cy="8" r="6" fill="none" stroke="#999" stroke-width="2.5"/><path d="M12.5 12.5l5 5" stroke="#999" stroke-width="3" stroke-linecap="round"/></svg>
  </div>
</header>

<section class="hero">
  <div class="hero-glow"></div>
  <div class="hero-render" role="img" aria-label="Rendered project image in the showcase slider"></div>
  <h1 class="hero-title">Engineering Sustainable Future</h1>
  <p class="hero-copy">We offer a broad range of services that are designed to support and nurture manufacturing companies and industries whether you are big or small.</p>
  <div class="hero-rule"></div>
  <div class="slide-arrow" style="left:135px;top:368px"><svg width="16" height="18" viewBox="0 0 16 18"><path d="M11 2L4 9l7 7" fill="none" stroke="#fff" stroke-width="3.5" stroke-linecap="round" stroke-linejoin="round"/></svg></div>
  <div class="slide-arrow" style="left:1001px;top:380px"><svg width="16" height="18" viewBox="0 0 16 18"><path d="M5 2l7 7-7 7" fill="none" stroke="#fff" stroke-width="3.5" stroke-linecap="round" stroke-linejoin="round"/></svg></div>
</section>

<main class="content-panel"></main>
<a class="showcase-tab" href="#"><span class="dot"><svg width="16" height="18" viewBox="0 0 16 18"><path d="M5 2l7 7-7 7" fill="none" stroke="#fff" stroke-width="3.5" stroke-linecap="round" stroke-linejoin="round"/></svg></span>Our showcase</a>

<h2 class="welcome-title">Welcome</h2>
<p class="welcome-copy" style="top:563px">TORQUE-LINE is a mechanical engineering and technology company focused on helping local&nbsp; manufacturing companies and local industries improve their products, services and sustainability through the application of engineering, technology and focused improvement.</p>
<p class="welcome-copy" style="top:615px">We offer a broad range of services that are designed to support and nurture manufacturing companies and industries whether you are big or small. We bring togther the services you would only find in a capital city to companies in North Queensland at a competitive rates. Our core services revolve around the application of the latest 3D Solid Modelling technology to assist in creating solutions to your mechanical design problems. These services are complemented by our Technology services which are designed to help your company leverage the latest technology to become globally competitive. Furthermore we offer a range of Focused Im-provement and Specialty services as we strive to bring you complete solutions to your business.</p>

<article class="service-card" style="left:156px">
  <div class="art" role="img" aria-label="Drafting compass over blueprint" style="left:20px;top:8px;width:70px;height:102px;background:linear-gradient(160deg,#cfe4f5,#5d8fc2)"></div>
  <h2 style="left:98px;top:20px">Engineering &amp; Design</h2>
  <p style="top:131px">We offer a broad range of services that are designed to support and nurture manufacturing companies and industries whether you are big or small. We bring togther the services</p>
  <a class="more" href="#" style="top:205px">Read More</a>
</article>
<article class="service-card" style="left:455px">
  <div class="art" role="img" aria-label="Specialist consultant figure" style="left:18px;top:10px;width:78px;height:110px;background:linear-gradient(180deg,#e9eef5,#7f98bd)"></div>
  <h2 style="left:106px;top:23px;color:#c9f3a6">Speciality Services</h2>
  <p style="top:131px">We offer a broad range of services that are designed to support and nurture manufacturing companies and industries whether you are big or small. We bring togther the services</p>
  <a class="more" href="#" style="top:205px">Read More</a>
</article>
<article class="service-card" style="left:760px">
  <div class="art" role="img" aria-label="Computer monitor" style="left:160px;top:16px;width:92px;height:82px;background:linear-gradient(160deg,#dfe8f2,#3d7ad0)"></div>
  <h2 style="left:16px;top:27px">Technology</h2>
  <p style="top:127px">We offer a broad range of services that are designed to support and nurture manufacturing companies and industries whether you are big or small. We bring togther the services</p>
  <a class="more" href="#" style="top:201px">Read More</a>
</article>

<footer class="site-footer">
  <p class="copyright">Copyright © 2009 TORQUE-LINE PTY LTD&nbsp;&nbsp;&nbsp;&nbsp; All Rights Reserved.</p>
  <a class="social" href="#" aria-label="Social profile" style="left:864px;background:#3b5da8"></a>
  <a class="social" href="#" aria-label="Social profile" style="left:911px;background:#3fb2e6"></a>
  <a class="social" href="#" aria-label="Social profile" style="left:962px;background:#2b88c4"></a>
  <a class="social" href="#" aria-label="Social profile" style="left:1011px;background:#e8e8e8"></a>
</footer>

</body>
</html>
```